High profile consultancy

We need a web design for a company called BK Services. BK as abbreviation for Bold Keystone.

Company focusses on Sourcing (BK Sourcing, focus on ICT), Metrics (BK Metrics; focus on business case analysis and trends in ICT) and Software (BK software; to be developed later on; mainly tools supporting BK soucing and metrics)

Customers base consists of large enterprises, >1000 employees.

Site needs to have menu's for
- services
- login
- about
and a special area ' inspire ' to be able to communicate topics that should inspire our customers to contact us.

but key; it schould communicate our expertise and focus on deep knowlegde of ICT sourcing

Reason: please advice on content management systems to be used to maintain site also please advice on Trovix search clickbids. Will provide feedback on designs shortly.

Target Market(s)

CIO's; board of directors;
company excels in ICT / business knowledge and ability to execute; creates / optimizes relations between ICT suppliers and enterprises.

Requirements
Must have
• website should be easily be found; adaptive by design; accessible by all browsers.
• Need to have a login section for later use
Nice to have
• usage of (draft) logo. see upload.

```html
<!DOCTYPE html>
<html lang="en">
<head>
<meta charset="utf-8">
<title>BK Services — Strategic Consulting</title>
<link href="https://fonts.googleapis.com/css2?family=Open+Sans:wght@400;600&display=swap" rel="stylesheet">
<style>
  :root {
    --page-bg: #58595b;
    --white: #ffffff;
    --ink: #222222;
    --body-text: #555555;
    --nav-top: #474747;
    --nav-bottom: #232323;
    --nav-line: #5e5e5e;
    --box-top: #3a3a3a;
    --box-bottom: #232323;
    --link: #39b7ec;
    --brand-blue: #1a5aa8;
    --brand-grey: #6b6b6b;
    --rule: #bdbdbd;
  }
  * { margin: 0; padding: 0; box-sizing: border-box; }
  html, body { width: 1200px; height: 1000px; overflow: hidden; }
  body {
    position: relative;
    background: var(--page-bg);
    font-family: "Open Sans", Arial, sans-serif;
    color: var(--ink);
  }
  .site-header {
    position: absolute; left: 0; top: 0; width: 1200px; height: 125px;
    background: var(--white); border-top: 2px solid #555;
  }
  .brand {
    position: absolute; left: 140px; top: 34px;
    display: flex; align-items: center; gap: 14px;
  }
  .brand-mark { width: 52px; height: 52px; border-radius: 50%; background: var(--brand-blue); }
  .brand-name { font-size: 40px; font-weight: 400; color: var(--brand-grey); letter-spacing: 1px; }
  .header-tools {
    position: absolute; right: 124px; top: 26px;
    display: flex; align-items: center; gap: 3px;
  }
  .header-login { font-size: 15px; color: var(--ink); margin-right: 10px; }
  .social { width: 21px; height: 21px; display: block; }
  .social.a { background: #d8493b; }
  .social.b { background: #3b5998; }
  .social.c { background: #1b86bc; }
  .social.d { background: #41b4e8; }

  .main-nav {
    position: absolute; left: 0; top: 125px; width: 1200px; height: 55px;
    background: linear-gradient(var(--nav-top), var(--nav-bottom));
  }
  .main-nav a {
    position: absolute; top: 15px; font-size: 15px; color: #eee; text-decoration: none;
  }
  .main-nav a.current { color: #fff; font-weight: 600; }
  .nav-sep { position: absolute; top: 7px; width: 1px; height: 38px; background: var(--nav-line); }

  .content {
    position: absolute; left: 120px; top: 178px; width: 960px; height: 822px;
    background: var(--white);
  }
  .hero {
    position: absolute; left: 0; top: 2px; width: 960px; height: 367px;
    background: linear-gradient(90deg, #b49a82 0%, #d9d2c8 30%, #8a7466 55%, #e6e2dc 75%, #5a6678 100%);
  }
  .hero-caption {
    position: absolute; left: 0; bottom: 0; width: 960px; height: 75px;
    background: rgba(20,20,20,0.82); color: #fff; padding: 12px 17px;
  }
  .hero-caption h2 { font-size: 20px; font-weight: 400; letter-spacing: .3px; }
  .hero-caption p { font-size: 14px; margin-top: 3px; }

  .welcome { position: absolute; left: 14px; top: 382px; width: 920px; }
  .welcome h1 { font-size: 20px; font-weight: 400; color: var(--ink); }
  .welcome p {
    font-size: 12px; line-height: 14px; color: var(--body-text); margin-top: 12px;
    letter-spacing: .4px; white-space: nowrap;
  }

  .feature {
    position: absolute; top: 484px; width: 305px; height: 183px;
    background: linear-gradient(var(--box-top), var(--box-bottom));
    color: #fff; padding: 15px 19px;
  }
  .feature h3 { font-size: 15px; font-weight: 400; margin-bottom: 10px; }
  .feature p { font-size: 11.5px; line-height: 13px; white-space: nowrap; }
  .feature .link { color: var(--link); }
  .feature .gap { margin-top: 13px; }
  .more {
    position: absolute; left: 20px; bottom: 16px; font-size: 12px; color: var(--link);
    text-decoration: none; display: flex; align-items: center; gap: 12px;
  }
  .more svg { width: 10px; height: 10px; }

  .industries { position: absolute; left: 13px; top: 685px; }
  .industries h4 { font-size: 13px; font-weight: 400; color: var(--ink); }
  .industry-col { position: absolute; top: 33px; font-size: 10.5px; line-height: 16px; color: #333; white-space: nowrap; letter-spacing: .2px; }
  .site-footer {
    position: absolute; left: 0; top: 789px; width: 960px; border-top: 1px solid var(--rule);
    text-align: center; font-size: 10.5px; color: #444; padding-top: 9px;
  }
</style>
</head>
<body>
  <header class="site-header">
    <div class="brand">
      <span class="brand-mark"></span>
      <span class="brand-name">BK Services</span>
    </div>
    <div class="header-tools">
      <span class="header-login">Login</span>
      <span class="social a" aria-label="Social network one"></span>
      <span class="social b" aria-label="Social network two"></span>
      <span class="social c" aria-label="Social network three"></span>
      <span class="social d" aria-label="Social network four"></span>
    </div>
  </header>

  <nav class="main-nav">
    <a class="current" style="left:296px">Home</a>
    <span class="nav-sep" style="left:378px"></span>
    <a style="left:417px">About Us</a>
    <span class="nav-sep" style="left:520px"></span>
    <a style="left:559px">Services</a>
    <span class="nav-sep" style="left:656px"></span>
    <a style="left:697px">Login</a>
    <span class="nav-sep" style="left:777px"></span>
    <a style="left:814px">contact us</a>
  </nav>

  <main class="content">
    <section class="hero" role="img" aria-label="Photo of six smiling business people in suits standing together in a bright office">
      <div class="hero-caption">
        <h2>STRATEGIC CONSULTING</h2>
        <p>Leaders lead differently when they know what Hallmere knows</p>
      </div>
    </section>

    <section class="welcome">
      <h1>Welcome</h1>
      <p>Welcome to BK Keystone-Advisory.example - your one stop resource for everything there is to know about consulting.If you're reading this, you have<br>taken the first step in getting your ideal consulting job. This site is the ultimate resource for prospective graduates looking for a consulting&nbsp; career.<br>We have an extensive database of information available to you, and it's entirely free Whether you are looking for a list of consulting firms, interview</p>
    </section>

    <article class="feature" style="left:14px">
      <h3 style="margin-top:2px">Insights</h3>
      <p class="link">How Technology is Reinventing the World of<br>Manufacturing</p>
      <p class="gap">We examine a few trends that are transforming<br>the manufacturing industry and what it means<br>for IT service providers going ahead.</p>
      <a class="more">More Insights <svg viewBox="0 0 10 10"><path d="M0 1 L10 5 L0 9 L3 5 Z" fill="#bbb"/></svg></a>
    </article>

    <article class="feature" style="left:328px">
      <h3>Mastering Digital Feedback</h3>
      <p>A Norvane 2013 Global Trend Study</p>
      <p class="gap">Learn how large companies are using social<br>media. A study of more than 650 executives<br>worldwide shows that social media has become<br>a key driver of marketing.</p>
      <a class="more">Read the findings of the study <svg viewBox="0 0 10 10"><path d="M0 1 L10 5 L0 9 L3 5 Z" fill="#bbb"/></svg></a>
    </article>

    <article class="feature" style="left:642px">
      <h3 style="margin-top:-2px">News &amp; Events</h3>
      <p class="link">Norvane Named a Global Leader in Vantix<br>MarketView: Worldwide Life Science Sales &amp;<br>Marketing ITO 2013</p>
      <p class="link gap">Kestra Ltd., the Hungarian CSD, selects Norvane<br>CoreLedger for platform modernization and S3X<br>settlement</p>
      <a class="more" style="left:18px">More News &amp; Events <svg viewBox="0 0 10 10"><path d="M0 1 L10 5 L0 9 L3 5 Z" fill="#bbb"/></svg></a>
    </article>

    <section class="industries">
      <h4>Industries</h4>
      <div class="industry-col" style="left:0">Banking &amp; Financial Services<br>Energy &amp; Utilities<br>Government</div>
      <div class="industry-col" style="left:232px">Healthcare<br>High Tech<br>Insurance</div>
      <div class="industry-col" style="left:466px">Life Sciences<br>Manufacturing<br>Media &amp; Information Services</div>
      <div class="industry-col" style="left:703px">Metals &amp; Mining<br>Retail &amp; Consumer Products<br>Retail &amp; Consumer Products</div>
    </section>

    <footer class="site-footer">© 2010-2013 BK Services Limited. All Rights Reserved</footer>
  </main>
</body>
</html>
```